Business software developers new website

We need to redesign our website. Our current website is http://www.plumvista.net/index.html, which is outdated and needs a new look. We moved out from web design and have concentrated more on the back end of the systems, for example, system support and security and cloud-based applications. Our major clients include both private and government sectors. We would like to see some designs that are all in one page, simple and clean. Prefer illustrator or obstructed images instead of real-life photos. Must look futuristic yet friendly. Attached the new logo for your references and good luck.

Target Market(s)

Medium to big company for their IT or data management. Either improve or upgrade their current system.

Industry/Entity Type

Business Software

Number of Pages Required

1 page

Colors

Designer to choose colors to be used in the design.

Requirements
Must have
• Simple and clean. Individual assets must be provided in the correct size and format(png or jpeg). Prefer Goggle fonts. Even though the logo color is red, grey and black, still prefer some modern colors that go well with red. When design, must consider the possibility to convert it into responsive.
Nice to have
• White background
Should not have
• real life photos, no slider

```html
<!DOCTYPE html>
<html lang="en">
<head>
<meta charset="utf-8">
<title>Plumvista.net — Business Software</title>
<link href="https://fonts.googleapis.com/css2?family=Roboto:wght@300;400;500&display=swap" rel="stylesheet">
<style>
:root{
  --red:#f42d2d;
  --ink:#111111;
  --text:#333333;
  --muted:#555555;
  --topbar:#232323;
  --band:#f2f2f2;
  --line:#cfcfcf;
  --white:#ffffff;
}
*{box-sizing:border-box;margin:0;padding:0}
html,body{width:1200px;height:2238px;overflow:hidden;background:var(--white)}
body{position:relative;font-family:'Roboto',sans-serif;color:var(--text)}
.abs{position:absolute}

.topbar{left:0;top:0;width:1200px;height:31px;background:var(--topbar)}
.topbar-phone{right:102px;top:9px;font-size:11px;font-weight:300;color:#ddd;display:flex;align-items:center;gap:3px}

.brand{left:99px;top:39px;font-size:13.5px;color:var(--ink)}
.nav{top:40px;font-size:12.5px;color:var(--ink)}
.nav a{color:inherit;text-decoration:none}
.nav .active{color:var(--red)}

.hero-title{left:184px;top:192px;font-size:28px;font-weight:400;line-height:40px;color:var(--ink)}
.hero-title .dot{color:var(--red)}
.hero-sub{left:184px;top:279px;font-size:17.5px;font-weight:300;line-height:31px;color:var(--muted)}
.btn{top:380px;height:40px;font-size:16px;display:flex;align-items:center;justify-content:center;border-radius:2px}
.btn-fill{left:184px;width:114px;background:var(--red);color:var(--white)}
.btn-line{left:325px;width:113px;border:1.5px solid var(--red);color:var(--red)}
.hero-art{left:676px;top:163px;width:410px;height:275px;background:linear-gradient(135deg,#ececec,#f6f6f6 60%,#fbe3e3)}

.divider{left:0;top:592px;width:1200px;height:1px;background:var(--line)}

.section-title{font-size:23px;font-weight:400;color:var(--ink)}
.company-title{left:184px;top:664px}
.rule{height:1px;background:var(--red)}
.company-rule{left:184px;top:703px;width:102px}
.company-text{left:184px;top:718px;width:490px;font-size:14.2px;font-weight:300;line-height:31px;color:var(--text)}
.company-more{left:184px;top:884px;font-size:14px;color:var(--red)}
.company-art{left:694px;top:838px;width:318px;height:170px;border-radius:60px 90px 80px 40px;background:linear-gradient(135deg,#eeeeee,#f4f4f4 55%,#f6c9c9)}

.faq-title{left:0;width:1200px;top:1132px;text-align:center}
.faq-rule{left:568px;top:1169px;width:64px;background:#555}
.faq-card{left:360px;top:1196px;width:481px;height:420px;background:var(--white);box-shadow:0 0 6px rgba(0,0,0,.14);text-align:center;padding:38px 20px 0}
.faq-q{font-size:14.5px;color:var(--red);margin-bottom:14px}
.faq-a{font-size:14.2px;font-weight:300;line-height:31px;color:var(--text);margin-bottom:20px}

.band{left:0;top:1684px;width:1200px;height:124px;background:var(--band)}
.footer{left:0;top:1808px;width:1200px;height:404px;background:var(--red);color:var(--white)}
.footer h2{position:absolute;font-size:24.5px;font-weight:400}
.philo-title{left:183px;top:34px}
.philo-text{left:184px;top:80px;width:460px;font-size:15px;font-weight:300;line-height:31px}
.contact-lines{left:184px;top:273px;font-size:15px;font-weight:300;line-height:27px}
.msg-title{left:665px;top:34px}
.field{border:1.5px solid var(--white);font-size:10.5px;font-weight:300;padding:9px 8px;color:#ffe3e3}
.field-name{left:666px;top:85px;width:147px;height:31px;padding-top:8px}
.field-reply{left:837px;top:85px;width:147px;height:31px;padding-top:8px}
.field-body{left:666px;top:139px;width:334px;height:99px}
.send{left:666px;top:264px;width:111px;height:30px;border:1.5px solid var(--white);font-size:10.5px;font-weight:500;display:flex;align-items:center;justify-content:center}
.copyright{left:184px;top:376px;font-size:11px;font-weight:300;display:flex;align-items:center;gap:4px}
.social{left:1004px;top:376px;width:11px;height:11px;border:1px solid var(--white);border-radius:50%}
</style>
</head>
<body>

<div class="abs topbar"></div>
<div class="abs topbar-phone">
  <svg width="10" height="10" viewBox="0 0 24 24" fill="none" stroke="#ddd" stroke-width="2"><path d="M22 16.9v3a2 2 0 0 1-2.2 2 19.8 19.8 0 0 1-8.6-3.1 19.5 19.5 0 0 1-6-6A19.8 19.8 0 0 1 2.1 4.2 2 2 0 0 1 4.1 2h3a2 2 0 0 1 2 1.7c.1 1 .4 1.9.7 2.8a2 2 0 0 1-.5 2.1L8 9.9a16 16 0 0 0 6 6l1.3-1.3a2 2 0 0 1 2.1-.4c.9.3 1.8.6 2.8.7a2 2 0 0 1 1.7 2z"/></svg>
  +61 7 5550 1824
</div>

<div class="abs brand">Plumvista.net</div>
<nav>
  <div class="abs nav" style="left:727px"><a class="active" href="#">Home</a></div>
  <div class="abs nav" style="left:814px"><a href="#">Our Services</a></div>
  <div class="abs nav" style="left:940px"><a href="#">Our Clients</a></div>
  <div class="abs nav" style="left:1056px"><a href="#">Contact</a></div>
</nav>

<h1 class="abs hero-title">We are solutions for a wide<br>variety of industries<span class="dot">.</span></h1>
<p class="abs hero-sub">We are known for the quality of our work, affordable rates<br>and our individual approach to each customer.</p>
<div class="abs btn btn-fill">Contact us</div>
<div class="abs btn btn-line">Read more</div>
<div class="abs hero-art" role="img" aria-label="Illustration of a person working at a laptop on a desk with a mug and plant, documents pinned on a board behind"></div>

<div class="abs divider"></div>

<h2 class="abs section-title company-title">Our Company</h2>
<div class="abs rule company-rule"></div>
<p class="abs company-text">Plumvista.net&nbsp; is an Australian based Software and Web Development Company that provides individual technology solutions and professional software for clients worldwide. Our work is based on quality sales, customer and technical support services. Being oriented towards innovative productivity in our work, we come up with essential tools for online .....</p>
<div class="abs company-more">Read More</div>
<div class="abs company-art" role="img" aria-label="Illustration of a developer seated at a desk with two red monitors in front of a window"></div>

<h2 class="abs section-title faq-title">FAQ</h2>
<div class="abs rule faq-rule"></div>
<div class="abs faq-card">
  <p class="faq-q">How much does a website powered by Plumvista.net cost?</p>
  <p class="faq-a">There are quite a few factors that are going to affect the ultimate cost of your web site. These factors include how many pages you are going to have, if you will sell products on your website, the graphic work involved, and how interactive your web site will be.</p>
  <p class="faq-q">How long does it take to have a website designed?</p>
  <p class="faq-a">Again it's all depends on how many pages and features you are going to have, if you will sell products on your website, the graphic work involved, and how interactive your web site will be.<br>Contact us for a free quote.</p>
</div>

<div class="abs band"></div>

<footer class="abs footer">
  <h2 class="philo-title">Philosophy</h2>
  <p class="abs philo-text">As web developers, we understand that a powerful and functional website is a vital component of modern day marketing for companies of today. This is why our web site development team work with all of our clients to ensure their web site design will deliver to their target market.</p>
  <p class="abs contact-lines">Phone: +61 7 5550 1824<br>Mobile: +61 0400 555 318</p>

  <h2 class="msg-title">Send us a messeage</h2>
  <div class="abs field field-name">What's your name?</div>
  <div class="abs field field-reply">Where I can reply?</div>
  <div class="abs field field-body">Talk to me</div>
  <div class="abs send">Send Messeage</div>

  <div class="abs copyright">
    <svg width="11" height="11" viewBox="0 0 12 12" fill="none" stroke="#fff" stroke-width="1"><circle cx="6" cy="6" r="5.2"/><path d="M7.8 4.4A2.2 2.2 0 1 0 7.8 7.6"/></svg>
    Copyright | 2019
  </div>
  <div class="abs social"></div>
</footer>

</body>
</html>
```